Business card design needed for Pollen Bakes

We need a new business card designed for our business. We create complete DIY cake kits to be delivered Australia Wide.

I would like our logo used (see attached).

Industry/Entity Type

Business

Contact Information for Business Card

Pollen Bakes - Complete DIY Cake Kits
www.pollenbakes.com.au
0472 315 904
sales@pollenbakes.com.au
www.friendnest.com/pollenbakes1

Requirements
Must have
• logo

```html
<!DOCTYPE html>
<html lang="en">
<head>
<meta charset="utf-8">
<title>Pollen Bakes – Business Card</title>
<link rel="stylesheet" href="https://fonts.googleapis.com/css2?family=Quicksand:wght@500;700&display=swap">
<style>
  :root {
    --backdrop: #3b3b3d;
    --card-core: #5e1a10;
    --card-edge: #2c0907;
    --frame-gold: #c9a46a;
    --stud-gold: #e2b652;
    --brand-red: #cf2e3f;
    --tagline-teal: #93c7bf;
    --icon-pink: #e48fb4;
    --text-light: #f3ece8;
    --mascot-hair: #8a5a3a;
    --mascot-pink: #e88bb8;
  }
  * { box-sizing: border-box; margin: 0; padding: 0; }
  html, body { width: 1200px; height: 1000px; overflow: hidden; }
  body {
    position: relative;
    background: var(--backdrop);
    font-family: "Quicksand", sans-serif;
    color: var(--text-light);
  }
  .card {
    position: absolute;
    left: 272px;
    width: 690px;
    height: 390px;
    background: radial-gradient(ellipse at 50% 45%, var(--card-core) 0%, #451109 55%, var(--card-edge) 100%);
  }
  .card--front { top: 87px; }
  .card--back { top: 521px; }
  .card__frame {
    position: absolute;
    inset: 16px;
    border: 1px solid var(--frame-gold);
    opacity: 0.8;
  }
  .card__stud {
    position: absolute;
    width: 8px; height: 8px;
    border-radius: 50%;
    background: var(--stud-gold);
  }
  .stud--tl { left: 13px; top: 13px; }
  .stud--tr { right: 13px; top: 13px; }
  .stud--bl { left: 13px; bottom: 13px; }
  .stud--br { right: 13px; bottom: 13px; }

  .mascot {
    position: absolute;
    border-radius: 14px;
    background: linear-gradient(160deg, var(--mascot-hair) 0%, #b77a6a 45%, var(--mascot-pink) 100%);
    opacity: 0.85;
  }
  .mascot--front { left: 256px; top: 68px; width: 172px; height: 146px; }
  .mascot--back { left: 498px; top: 227px; width: 170px; height: 147px; }

  .brand-name {
    color: var(--brand-red);
    font-weight: 700;
    line-height: 1;
    white-space: nowrap;
  }
  .tagline {
    color: var(--tagline-teal);
    font-weight: 700;
    white-space: nowrap;
  }

  /* Front */
  .front-logo {
    position: absolute;
    left: 0; right: 0; top: 224px;
    text-align: center;
  }
  .front-logo .brand-name { font-size: 38px; }
  .front-logo .tagline { font-size: 13px; margin-top: 8px; letter-spacing: 0.3px; }
  .front-url {
    position: absolute;
    left: 0; right: 0; top: 328px;
    text-align: center;
    font-size: 13px;
    font-weight: 500;
    letter-spacing: 0.6px;
  }

  /* Back */
  .back-logo {
    position: absolute;
    left: 52px; top: 70px;
  }
  .back-logo .brand-name { font-size: 58px; }
  .back-logo .tagline { font-size: 19px; margin-top: 10px; margin-left: 78px; }

  .contact-list {
    position: absolute;
    left: 132px; top: 244px;
    list-style: none;
  }
  .contact-list li {
    display: flex;
    align-items: center;
    height: 23px;
    font-size: 12.5px;
    font-weight: 500;
    letter-spacing: 0.5px;
    white-space: nowrap;
  }
  .contact-list svg {
    width: 20px; height: 16px;
    margin-right: 20px;
    fill: var(--icon-pink);
    stroke: var(--icon-pink);
  }
</style>
</head>
<body>

<section class="card card--front" aria-label="Business card front">
  <div class="card__frame"></div>
  <span class="card__stud stud--tl"></span><span class="card__stud stud--tr"></span>
  <span class="card__stud stud--bl"></span><span class="card__stud stud--br"></span>
  <div class="mascot mascot--front" role="img" aria-label="Illustrated baker mascot holding a piping bag and a cupcake"></div>
  <div class="front-logo">
    <div class="brand-name">Pollen Bakes</div>
    <div class="tagline">complete DIY cake kits</div>
  </div>
  <div class="front-url">www.pollenbakes.com.au</div>
</section>

<section class="card card--back" aria-label="Business card back">
  <div class="card__frame"></div>
  <span class="card__stud stud--tl"></span><span class="card__stud stud--tr"></span>
  <span class="card__stud stud--bl"></span><span class="card__stud stud--br"></span>
  <div class="back-logo">
    <div class="brand-name">Pollen Bakes</div>
    <div class="tagline">complete DIY cake kits</div>
  </div>
  <ul class="contact-list">
    <li>
      <svg viewBox="0 0 20 16" aria-hidden="true"><path stroke="none" d="M2 5 Q10 0 18 5 L18 7 L14 7 L14 5 L6 5 L6 7 L2 7 Z M5 8 L15 8 L17 15 L3 15 Z"/><circle cx="10" cy="11.5" r="2" fill="#4a1009" stroke="none"/></svg>
      0472 315 904
    </li>
    <li>
      <svg viewBox="0 0 20 16" aria-hidden="true"><rect x="1" y="2" width="18" height="12" stroke="none"/><path d="M1.5 2.5 L10 9 L18.5 2.5" fill="none" stroke="#4a1009" stroke-width="1.3"/></svg>
      sales@pollenbakes.com.au
    </li>
    <li>
      <svg viewBox="0 0 20 16" aria-hidden="true"><g fill="none" stroke-width="1.3"><circle cx="10" cy="8" r="7"/><ellipse cx="10" cy="8" rx="3" ry="7"/><line x1="3" y1="8" x2="17" y2="8"/><line x1="4" y1="4.5" x2="16" y2="4.5"/><line x1="4" y1="11.5" x2="16" y2="11.5"/></g></svg>
      www.pollenbakes.com.au
    </li>
    <li>
      <svg viewBox="0 0 20 16" aria-hidden="true"><circle cx="10" cy="8" r="4" stroke="none"/></svg>
      www.friendnest.com/pollenbakes1
    </li>
  </ul>
  <div class="mascot mascot--back" role="img" aria-label="Illustrated baker mascot holding a piping bag and a cupcake"></div>
</section>

</body>
</html>
```